Sponsorenmappe für die Lindenhof Jugend Bewegungs Institut
Zielgruppe
Die Lindenhof Jugend Bewegungs Institut (LJBI) bietet Schulen und Vereinen vielfältige Sport-, Bewegungs- und Ernährungsangebote.
Mit der Lindenhof Jugend Kick Institut (LJKI) und der Jugend Kick Institut (JKI) hat die LJBI-GmbH für den Fußballbereich zwei eigene Marken.
Das ganzheitliche LJBI-Konzept fördert ein sinnvolles Zusammenspiel von Schule, Sport und Persönlichkeitsentwicklung.
Das Design der Sponsorenmappe sollte natürlich in erster Linie den (vorallem mittelständischen) potentiellen Sponsoren gefallen und diese ansprechen. Hier sollte das Design klar und strukturiert sein, jedoch kleine Einflüsse der kinderaffinenen Marken besitzen.
Aufgabenstellung
Anbei haben wir schon einmal eine "Sponsorenmappe" in Word entworfen. Hierbei handelt es sich nur um einen kleinen Vorschlag wie es vielleicht aussehen könnte!
Die Textbausteine sollen jedoch verwendet werden.
Format: Din A4 - Druckdatenblatt von Papierwelle liegt bei.
Vorder- und Rückseite der Broschüre sind schon angefertig! Diese müssen noch noch angefügt werden. Tendenziell sollte die Broschüre dieses Design aufgreifen. Auch die erste Klappseite (Auf dem Druckdatenblatt als "E" gekennzeichnet - bei "D") ist schon designt. Hierbei handelt es sich um das Organigramm der LJBI (siehe Anhang). Überschrift muss jedoch noch in der jeweiligen Schriftart eingefügt werden.
Anbei finden Sie eine Win-Rar-Datei mit Logos und Bildern, die Ihnen zur Verwendung stehen.
Zudem unsere Broschüre für weitere Infos
Dem Rest geben wir küntlerische Freiheit.

```html
<!DOCTYPE html>
<html lang="de">
<head>
<meta charset="utf-8">
<title>Sponsorenmappe LJBI</title>
<link rel="stylesheet" href="https://fonts.googleapis.com/css2?family=Barlow+Condensed:wght@400;500;600;700&display=swap">
<style>
:root{
  --sky-top:#6f8fcf;
  --sky-mid:#a9c0e4;
  --sky-low:#dfe8f2;
  --field:#5e9a3a;
  --field-light:#8dbb55;
  --track:#b5493a;
  --track-dark:#9a3a2e;
  --navy:#1d2350;
  --ink:#1a1a1a;
  --panel:rgba(255,255,255,0.93);
  --yellow:#f7d417;
  --accent:#2a8fd6;
  --shirt:#74d13a;
  --fold:rgba(255,255,255,0.8);
}
*{box-sizing:border-box;margin:0;padding:0}
html,body{width:1200px;height:663px;overflow:hidden;background:#fff}
body{font-family:"Barlow Condensed",sans-serif;color:var(--ink)}
.sheet{position:relative;width:1200px;height:663px;overflow:hidden}
.scene{position:absolute;inset:0;background:
  linear-gradient(180deg,var(--sky-top) 0%,var(--sky-mid) 35%,var(--sky-low) 58%,var(--field-light) 62%,var(--field) 67%,var(--track) 70%,var(--track-dark) 100%)}
.fold-lines{position:absolute;inset:0}
.abs{position:absolute}
.box{position:absolute;background:var(--panel)}
.logo-name{left:128px;top:33px;font-weight:600;color:var(--navy);font-size:18px;line-height:17px;text-transform:uppercase}
.quote{padding:6px 11px;font-size:7.4px;line-height:10.2px;font-weight:500}
.quote small{display:block;font-size:4.6px;line-height:6px;margin-top:2px;font-weight:400}
.tag{font-weight:600;font-size:17px;color:#111;display:flex;align-items:center;justify-content:center}
.arrow{position:absolute}
.photo-round{position:absolute;left:134px;top:174px;width:126px;height:126px;border-radius:50%;background:radial-gradient(circle,#c9a48a 0%,#6a7a4a 55%,#3d5a2c 100%);border:8px solid #e9edf2}
.band{font-weight:600;font-size:17px;text-align:center;line-height:23px}
.offer{padding:5px 8px;text-align:center}
.offer h3{font-weight:600;font-size:9.6px;margin-bottom:4px}
.offer p{font-size:5.2px;line-height:8px}
.team{padding:7px 10px;display:flex;gap:12px}
.team .col{flex:1;font-size:5.2px;line-height:7.2px}
.team h4{font-weight:600;font-size:7.4px;margin-bottom:5px}
.team ul{list-style:none;margin-top:4px}
.team li{font-size:7px;line-height:9.6px;font-weight:500;margin-bottom:2px}
.team .lead{font-size:7.4px;line-height:9.6px;font-weight:600;margin-bottom:5px}
.team p{margin-bottom:4px}
.section-title{left:440px;top:32px;color:#fff;font-size:16px;font-weight:400}
.card{position:absolute;background:var(--panel)}
.photo{position:absolute;background:#fff;padding:4px;box-shadow:0 1px 3px rgba(0,0,0,.35)}
.photo i{display:block;width:100%;height:100%;background:linear-gradient(180deg,#b8cde2 0%,#6a92b8 30%,#5aa83a 45%,var(--shirt) 62%,#d8c9a8 80%,#c7b591 100%)}
.h-card{font-weight:600;font-size:11px}
.txt{font-size:6.8px;line-height:10px}
.txt b{font-weight:600}
.list{list-style:none}
.list li::before{content:"• "}
.badge{position:absolute;border-radius:50%;background:var(--yellow);display:flex;flex-direction:column;align-items:center;justify-content:center;font-weight:600;font-size:6px;line-height:7.4px;text-align:center}
.partner{position:absolute;font-weight:600;color:var(--navy);display:flex;align-items:center;gap:4px}
.partner .sq{width:10px;height:10px;background:var(--accent)}
</style>
</head>
<body>
<main class="sheet">
  <div class="scene" role="img" aria-label="Sportplatz mit blauem Himmel, grünem Rasen und roter Laufbahn"></div>

  <svg class="fold-lines" width="1200" height="663" viewBox="0 0 1200 663" aria-hidden="true">
    <g fill="none" stroke="var(--fold)" stroke-width="0.8" stroke-dasharray="3 3">
      <line x1="402" y1="0" x2="402" y2="551"/>
      <line x1="801" y1="0" x2="801" y2="551"/>
    </g>
    <g fill="none" stroke="var(--fold)" stroke-width="0.8">
      <line x1="0" y1="551" x2="1200" y2="551"/>
      <polyline points="405,551 405,623 460,663"/>
      <polyline points="801,551 801,623 746,663"/>
    </g>
  </svg>

  <div class="abs logo-name">Lindenhof Jugend<br>Bewegungs Institut GmbH</div>

  <div class="box quote" style="left:39px;top:89px;width:153px;height:77px">
    „Kinder sollten mehr spielen, als viele Kinder es heutzutage tun. Denn wenn man genügend spielt, solange man klein ist, dann trägt man Schätze mit sich herum, aus denen man später sein ganzes Leben lang schöpfen kann.“
    <small>Marta Lindqvist (1907 – 2002), schwedische Schriftstellerin</small>
  </div>
  <div class="box quote" style="left:202px;top:89px;width:153px;height:77px">
    GENERELL GILT:<br>Kinder bewegen sich weniger und treiben immer seltener Sport. 40 – 60 % der Kinder haben Haltungsschwächen oder Haltungsschäden.
    <small>BEKI-Studie (Bewegte Kindheit Interventionsstudie) der Sportwissenschaftlichen Hochschule Altenau</small>
  </div>

  <div class="box tag" style="left:39px;top:174px;width:81px;height:30px">Spaß</div>
  <div class="box tag" style="left:274px;top:174px;width:81px;height:30px">Bewegung</div>
  <svg class="arrow" style="left:64px;top:204px" width="32" height="96" viewBox="0 0 32 96" aria-hidden="true"><path d="M12 0h8v80h12L16 96 0 80h12z" fill="#eef2f6"/></svg>
  <svg class="arrow" style="left:298px;top:204px" width="32" height="96" viewBox="0 0 32 96" aria-hidden="true"><path d="M12 0h8v80h12L16 96 0 80h12z" fill="#eef2f6"/></svg>
  <div class="photo-round" role="img" aria-label="Foto: aufeinandergelegte Kinderhände als Teamzeichen"></div>

  <div class="box band" style="left:39px;top:307px;width:316px;height:24px">Entwicklung</div>

  <div class="box offer" style="left:39px;top:338px;width:316px;height:57px">
    <h3>Die LJBI bietet vielfältige Sport-, Bewegungs- und Ernährungsangebote</h3>
    <p>• Das ganzheitliche LJBI-Konzept fördert ein sinnvolles Zusammenspiel von Schule, Sport und Persönlichkeitsentwicklung.<br>
    • Spaß und Freude sollen Kinder und Jugendliche langfristig für Sport und Bewegung motivieren.<br>
    • Dabei Eltern entlasten, Kinder fördern, zahlreiche Sport- und Bewegungsangebote schaffen, Gesundheitsschäden vorbeugen und das soziale Verhalten und den Teamgeist der Kinder stärken.</p>
  </div>

  <div class="box team" style="left:39px;top:403px;width:316px;height:135px">
    <div class="col">
      <h4>TEAM</h4>
      <p>Die qualifizierten, haupt- und nebenberuflichen Mitarbeiter in den verschiedenen Bereichen der LJBI haben langjährige Erfahrung im Kinder- und Jugendsport.</p>
      <p>Alle Übungsleiter und Lehrkräfte im Bereich unserer Sportangebote verfügen mindestens über ein:</p>
      <ul>
        <li>• Grundstudium in einem pädagogischen, sozial- oder sportwissenschaftlichen Studiengang,</li>
        <li>• haben eine spezifische Ausbildung oder</li>
        <li>• Übungsleiter-Lizenz.</li>
      </ul>
    </div>
    <div class="col">
      <h4>PHILOSOPHIE</h4>
      <p class="lead">„Bei sämtlichen Angeboten der LJBI steht stets der Spaß im Vordergrund.“</p>
      <p><b>Denn:</b> Wer mit Freude lernt, lernt schneller und nachhaltiger! Neben der sportlichen Ausbildung sollen die Kinder lernen, sich in einer Gruppe zu bewegen, soziale Kontakte zu knüpfen sowie Werten wie Fair Play, Disziplin und Gesundheitsbewusstsein mehr Bedeutung zuzuordnen.</p>
      <p><b>Unser Anspruch:</b> hohe Qualität aller angebotenen Leistungen – optimale Beratung, Organisation und Betreuung – gute Zusammenarbeit mit den Kindern, Eltern und Kooperationspartnern.</p>
    </div>
  </div>

  <h2 class="abs section-title">Kompetenz und Angebote</h2>

  <section class="card" style="left:422px;top:56px;width:346px;height:164px;transform:rotate(-1.2deg)">
    <div class="h-card abs" style="left:120px;top:6px">CAMPS &amp; SPEZIALTRAINING</div>
    <div class="partner" style="left:122px;top:40px;font-size:16px"><span class="sq"></span>JKI</div>
    <ul class="list txt abs" style="left:218px;top:22px;line-height:9px">
      <li>Für Mädchen und Jungen</li>
      <li>Von 5 bis 17 Jahren<br>&nbsp;&nbsp;(verschiedene Altersgruppen)</li>
      <li>2-bis 5-Tage-Camps.</li>
    </ul>
    <div class="txt abs" style="left:122px;top:67px">Camps pro Jahr (2015): 15 – 20<br>Tendenz 2016: &nbsp;&nbsp;&nbsp;&nbsp;&nbsp;&nbsp;&nbsp;30 – 40</div>
    <div class="txt abs" style="left:122px;top:90px">KINDER IM SCHNITT:<br>Pro Camp (2015): &nbsp;&nbsp;30 – 40<br>Tendenz 2016: &nbsp;&nbsp;&nbsp;&nbsp;&nbsp;&nbsp;40 – 50</div>
    <div class="partner" style="left:122px;top:140px;font-size:8px">Tempokids</div>
    <div class="partner" style="left:172px;top:133px;font-size:14px">movari.de</div>
    <div class="txt abs" style="left:237px;top:68px;text-align:center;font-weight:600">Regionale Wahrnehmung<br>eines Camps:</div>
    <div class="badge" style="left:240px;top:95px;width:36px;height:36px">Flyer<br>500</div>
    <div class="badge" style="left:282px;top:95px;width:36px;height:36px">Poster<br>15</div>
    <div class="badge" style="left:261px;top:128px;width:36px;height:36px">Personen<br>1200–2500</div>
  </section>
  <div class="photo" style="left:426px;top:58px;width:104px;height:78px;transform:rotate(-4deg)" role="img" aria-label="Gruppenfoto: Kinder in grünen Trikots am Strand"><i></i></div>
  <div class="photo" style="left:424px;top:134px;width:104px;height:78px;transform:rotate(2deg)" role="img" aria-label="Gruppenfoto: Kinder in grünen Trikots am Strand"><i></i></div>

  <section class="card" style="left:442px;top:221px;width:341px;height:82px"></section>
  <section class="card" style="left:445px;top:303px;width:335px;height:81px;background:rgba(255,255,255,0.6)"></section>
  <div class="txt abs" style="left:456px;top:228px;width:196px;text-align:justify"><span class="h-card">REISEN |</span> In Kooperation mit unseren Reisepartnern Nordlicht Reisen und Sonnenweg Touristik veranstaltet die JKI Reisen ins Ausland in Verbindung mit Fußballcamps. Professionelle Mitarbeiter, Trainer und Betreuer der Lindenhof Jugend Kick Institut (LJKI) sind bei den Camps vor Ort.</div>
  <div class="txt abs" style="left:456px;top:286px"><b>Tendenz 2016:</b><ul class="list"><li>8 Camps</li><li>25 – 30 Teilnehmer pro Reise</li><li>Türkei, Mallorca, Deutschland, . . .</li></ul></div>
  <div class="partner" style="left:576px;top:288px;font-size:7px;flex-direction:column;gap:2px"><span class="sq" style="width:32px;height:32px"></span>Nordlicht</div>
  <div class="partner" style="left:618px;top:300px;font-size:7px;width:36px;text-align:center">Sonnenweg Touristik</div>
  <div class="txt abs" style="left:514px;top:329px;font-weight:600">Akquise von Teilnehmern:</div>
  <div class="badge" style="left:475px;top:344px;width:35px;height:35px">Kataloge<br>150.000</div>
  <div class="badge" style="left:516px;top:344px;width:35px;height:35px">Messen<br>2 – 3</div>
  <div class="badge" style="left:557px;top:344px;width:35px;height:35px">Camps<br>30 – 40</div>
  <div class="badge" style="left:598px;top:344px;width:35px;height:35px">Flyer<br>ca. 5.000</div>
  <div class="photo" style="left:664px;top:234px;width:108px;height:80px;transform:rotate(-3deg)" role="img" aria-label="Gruppenfoto: Kinder in grünen Trikots am Strand"><i></i></div>
  <div class="photo" style="left:662px;top:314px;width:106px;height:72px;transform:rotate(3deg)" role="img" aria-label="Gruppenfoto: Kinder in grünen Trikots am Strand"><i></i></div>

  <section class="card" style="left:421px;top:386px;width:348px;height:165px;transform:rotate(0.8deg)"></section>
  <div class="abs txt" style="left:560px;top:404px;width:198px;transform:rotate(2deg);text-align:justify"><span class="h-card">SCHULKOOPERATIONEN |</span> Die LJBI bietet Schulen kostenfreie und ganzheitliche Konzepte sowie umfangreiche, sportartübergreifende und sportartspezifische Angebote in folgenden Bereichen an:
    <ul class="list" style="margin-top:6px">
      <li>Schulsport-Arbeitsgemeinschaften (AGs)</li>
      <li>Schulsporttage</li>
      <li>Schulturniere und -veranstaltungen</li>
      <li>Gesundheit, Prävention und Ernährung</li>
    </ul>
    <p style="margin-top:6px">Sporttage 2015: 10 – 15<br>Tendenz 2016: 40 – 60</p>
    <p style="margin-top:6px;font-weight:600">So wurden 2015 etwa 400 – 600 Kinder für eine aktive Lebensweise begeistert.</p>
  </div>
  <div class="photo" style="left:442px;top:384px;width:108px;height:80px;transform:rotate(4deg)" role="img" aria-label="Gruppenfoto: Kinder in grünen Trikots am Strand"><i></i></div>
  <div class="photo" style="left:424px;top:464px;width:106px;height:74px;transform:rotate(1.5deg)" role="img" aria-label="Gruppenfoto: Kinder in grünen Trikots am Strand"><i></i></div>
</main>
</body>
</html>
```